Visitenkarten-Design für Sonnen-/Fensterschutz
Zielgruppe
KLR GmbH ist eine Firma, die Sonnenschutz und Fensterschutz anbieten.
'Ihr kompetenter Partner in Sachen Sonnenschutz- , Fenster- und Türtechnik. Sie erhalten echtes Handwerk aus dem Mühlviertel zu fairen Preisen.'
Unsere Zielgruppe sind Personen mit Haus, die am Land leben.
Firmenname: KLR GmbH
Slogan: Fenster & Sonnenschutz
Aufgabenstellung
Hier befindet sich das Logodesign: https://dl.qv/t-Rm8pQ2wZtB
Bitte ein schlichtes Design bereitstellen mit einer Dummy-Person:
Lutz Brenneke + Telefonnummer + Email
Die finalen Daten bitte erst am Schluss berücksichtigen (für Gewinnerdesign)
Gerne auch hintern + vorne bedruckbar bereitstellen.

```html
<!DOCTYPE html>
<html lang="de">
<head>
<meta charset="utf-8">
<title>KLR GmbH – Visitenkarte</title>
<link rel="stylesheet" href="https://fonts.googleapis.com/css2?family=Poppins:ital,wght@0,600;1,400;1,500&family=Marck+Script&display=swap">
<style>
  :root {
    --stage: #585858;
    --paper: #ffffff;
    --ink: #555555;
    --brand-red: #d9302a;
    --brand-orange: #e0622a;
    --brand-deep: #d52a27;
  }
  * { margin: 0; padding: 0; box-sizing: border-box; }
  html, body { width: 1200px; height: 1200px; overflow: hidden; }
  body {
    background: var(--stage);
    position: relative;
    font-family: "Poppins", sans-serif;
  }
  .card {
    position: absolute;
    left: 280px;
    width: 669px;
    height: 433px;
    overflow: hidden;
  }
  .card-front { top: 130px; background: var(--paper); }
  .card-back {
    top: 635px;
    background: linear-gradient(90deg, var(--brand-orange) 0%, var(--brand-deep) 78%, var(--brand-deep) 100%);
  }

  .divider {
    position: absolute;
    left: 350px;
    top: 28px;
    width: 2px;
    height: 380px;
    background: linear-gradient(180deg, rgba(217,48,42,0) 0%, var(--brand-red) 20%, var(--brand-red) 80%, rgba(217,48,42,0) 100%);
  }

  .brand {
    position: absolute;
    left: 60px;
    top: 196px;
    display: flex;
    align-items: center;
    gap: 14px;
  }
  .brand-mark {
    width: 34px;
    height: 34px;
    background: var(--brand-red);
  }
  .brand-name {
    font-weight: 600;
    font-size: 38px;
    line-height: 1;
    color: var(--brand-red);
    letter-spacing: 1px;
  }

  .person {
    position: absolute;
    left: 352px;
    width: 317px;
    top: 70px;
    text-align: center;
    font-style: italic;
    color: var(--ink);
  }
  .person-name { font-size: 20px; font-weight: 400; letter-spacing: 0.3px; }
  .person-role { font-size: 15px; font-weight: 500; margin-top: 6px; }

  .contact {
    position: absolute;
    left: 381px;
    top: 238px;
    font-style: italic;
    color: var(--ink);
  }
  .contact-company { font-size: 19px; margin-bottom: 10px; }
  .contact-company .accent { color: var(--brand-red); }
  .contact-address { font-size: 16px; line-height: 27px; margin-bottom: 8px; }
  .contact-line { font-size: 16px; line-height: 28px; }
  .contact-line .label { color: var(--brand-red); }

  .back-watermark {
    position: absolute;
    left: 0; right: 0;
    top: 120px;
    text-align: center;
    font-weight: 600;
    font-size: 170px;
    line-height: 1;
    color: rgba(255,255,255,0.12);
  }
  .slogan {
    position: absolute;
    left: 50%;
    top: 215px;
    transform: translateX(-50%) rotate(-15deg);
    white-space: nowrap;
    font-family: "Marck Script", cursive;
    font-size: 66px;
    color: #ffffff;
  }
</style>
</head>
<body>
  <section class="card card-front">
    <div class="brand">
      <span class="brand-mark"></span>
      <span class="brand-name">KLR GmbH</span>
    </div>
    <div class="divider"></div>
    <div class="person">
      <p class="person-name">Lutz Brenneke</p>
      <p class="person-role">Geschäftsführer</p>
    </div>
    <div class="contact">
      <p class="contact-company"><span class="accent">KLR</span> GmbH</p>
      <p class="contact-address">Am Lindenfeld 7-9<br>30519 Hannover</p>
      <p class="contact-line"><span class="label">Tel.:</span>+49 151 204 6381</p>
      <p class="contact-line"><span class="label">Mail:</span> info@klr-fenster.de</p>
    </div>
  </section>

  <section class="card card-back">
    <div class="back-watermark">KLR</div>
    <p class="slogan">Fenster &amp; Sonnenschutz</p>
  </section>
</body>
</html>
```